Business card design needed

We need a business card for a new business. We are called Tiny Toilers Gear, and we make replica kid size clothing, mainly hi vis shirts, work trousers and shorts. Our long term goal is to include clothing for numerous trades and professions, for our littlest Aussies. We would like a kid friendly card using navy blue, bright orange, bright yellow and bright pink. We haven't set up our web page yet because we want to base it on our final business card design.
Updates

Industry/Entity Type

Clothing

```html
<!DOCTYPE html>
<html lang="en">
<head>
<meta charset="utf-8">
<title>Tiny Toilers Gear – Business Card</title>
<link rel="stylesheet" href="https://fonts.googleapis.com/css2?family=Poppins:wght@500;600&display=swap">
<style>
  :root {
    --page-bg: #8a8a8a;
    --page-bg-light: #b4b4b4;
    --sky-deep: #0a5fa8;
    --sky-mid: #1796d8;
    --sky-light: #4fc3f0;
    --pattern-blue: #3fa9dd;
    --pattern-blue-light: #6cc4ea;
    --band-yellow: #f7c21a;
    --band-yellow-deep: #f0a80c;
    --accent-pink: #e6199b;
    --ink-navy: #14213d;
    --logo-white: #ffffff;
    --divider: #14213d;
  }
  html, body {
    margin: 0;
    padding: 0;
    overflow: hidden;
  }
  body {
    width: 724px;
    height: 1200px;
    background: radial-gradient(ellipse at 50% 35%, var(--page-bg-light), var(--page-bg) 75%);
    font-family: "Poppins", sans-serif;
    position: relative;
  }
  .card {
    position: absolute;
    left: 82px;
    width: 560px;
    height: 320px;
    clip-path: polygon(0 0, 92% 0, 100% 14%, 100% 100%, 8% 100%, 0 86%);
    overflow: hidden;
  }
  .card--front { top: 170px; }
  .card--back { top: 620px; }

  .card-front__sky {
    position: absolute;
    inset: 0;
    background: radial-gradient(ellipse at 45% 45%, var(--sky-light), var(--sky-mid) 45%, var(--sky-deep) 100%);
  }
  .card-front__brand {
    position: absolute;
    top: 50%;
    left: 0;
    right: 0;
    transform: translateY(-50%);
    display: flex;
    align-items: center;
    justify-content: center;
    gap: 14px;
  }
  .card-front__dot {
    width: 26px;
    height: 26px;
    border-radius: 50%;
    background: var(--accent-pink);
    flex: none;
  }
  .card-front__name {
    margin: 0;
    font-weight: 600;
    font-size: 44px;
    letter-spacing: -0.5px;
    color: var(--logo-white);
    white-space: nowrap;
  }
  .card-front__tab {
    position: absolute;
    right: 8px;
    top: 50%;
    width: 30px;
    height: 30px;
    transform: translateY(-50%);
  }

  .card-back__pattern {
    position: absolute;
    left: 0;
    top: 0;
    width: 100%;
    height: 246px;
    background: linear-gradient(180deg, var(--pattern-blue-light), var(--pattern-blue));
  }
  .card-back__divider {
    position: absolute;
    left: 50%;
    top: 26px;
    width: 1.5px;
    height: 196px;
    background: var(--divider);
  }
  .card-back__column {
    position: absolute;
    top: 92px;
    width: 230px;
    margin: 0;
    padding: 0;
    list-style: none;
    color: var(--ink-navy);
    font-weight: 500;
    font-size: 13px;
    line-height: 19px;
  }
  .card-back__column--left { left: 36px; }
  .card-back__column--right { left: 302px; }
  .card-back__band {
    position: absolute;
    left: 0;
    bottom: 0;
    width: 100%;
    height: 74px;
    background: linear-gradient(180deg, var(--band-yellow), var(--band-yellow-deep));
    display: flex;
    flex-direction: column;
    justify-content: center;
    align-items: center;
    color: var(--ink-navy);
    font-weight: 500;
    font-size: 13px;
    line-height: 18px;
  }
  .card-back__band p { margin: 0; }
</style>
</head>
<body>

  <section class="card card--front" aria-label="Business card front">
    <div class="card-front__sky" role="img" aria-label="Starry blue sky texture"></div>
    <div class="card-front__brand">
      <span class="card-front__dot" aria-hidden="true"></span>
      <h1 class="card-front__name">Tiny Toilers Gear</h1>
    </div>
    <svg class="card-front__tab" viewBox="0 0 30 30" aria-hidden="true">
      <circle cx="15" cy="15" r="14" fill="var(--band-yellow)"/>
      <path d="M8 10 L12 15 L8 20 M13 10 L17 15 L13 20" fill="none" stroke="var(--ink-navy)" stroke-width="2.2" stroke-linecap="round" stroke-linejoin="round"/>
    </svg>
  </section>

  <section class="card card--back" aria-label="Business card back">
    <div class="card-back__pattern" role="img" aria-label="Faint pattern of small child figures on blue"></div>
    <div class="card-back__divider"></div>
    <ul class="card-back__column card-back__column--left">
      <li>Kid size hi vis shirts</li>
      <li>Work trousers and shorts</li>
      <li>For our littlest Aussies</li>
    </ul>
    <ul class="card-back__column card-back__column--right">
      <li>Call us for orders</li>
      <li>Sizes for ages two to ten</li>
      <li>Made for little workers</li>
    </ul>
    <div class="card-back__band">
      <p>Replica workwear for tiny tradies</p>
      <p>Hi vis, trousers and shorts</p>
      <p>Website coming soon</p>
    </div>
  </section>

</body>
</html>
```